Brelvo Pizza & Pasta Takeaway Flyer

Our takeaway shop needs a well designed flyer for print and letter box distribution. Design to have a clear list of menu, Specials, contact details. If menu doesn't fit into A4, we won't mind going upto extended A4. I have attached draft copy of our menu and list of item in excel. Please add 5mm Bleed to the flyer.
Flyer will get printed on 115gsm Gloss stock.

```html
<!DOCTYPE html>
<html lang="en">
<head>
<meta charset="utf-8">
<title>Brelvo Pizza & Pasta – Takeaway Menu</title>
<link href="https://fonts.googleapis.com/css2?family=Open+Sans:ital,wght@0,400;0,600;1,400&family=Dancing+Script:wght@700&family=Great+Vibes&family=Oswald:wght@400&display=swap" rel="stylesheet">
<style>
:root{
  --bg:#262626;
  --panel:#2b2b2b;
  --green:#8cc63f;
  --green-light:#a9d65a;
  --green-dark:#6fa52a;
  --price:#c9352f;
  --ring:#9e2a2b;
  --text:#f2f2f2;
  --dots:#e8e8e8;
}
*{margin:0;padding:0;box-sizing:border-box}
html,body{width:1200px;height:848px;overflow:hidden;background:var(--bg)}
.flyer{position:relative;width:1200px;height:848px;overflow:hidden;background:var(--bg);font-family:"Open Sans",Arial,sans-serif;color:var(--text)}
.section{position:absolute;background:var(--panel);overflow:hidden}
.bar{height:32px;background:linear-gradient(var(--green-light),var(--green) 60%,var(--green-dark));border-bottom:1px solid #cfe8a8;padding-left:44px;font-family:"Dancing Script",cursive;font-size:22px;line-height:32px;color:#fff;letter-spacing:.5px}
.list{position:absolute;left:11px;right:10px}
.row{display:flex;align-items:baseline;height:16px;font-size:13px;line-height:16px;color:var(--green);white-space:nowrap}
.row.solo{margin-bottom:9.6px}
.row small{font-size:10.5px;font-style:italic;color:var(--text);margin-left:3px}
.leader{flex:1;border-bottom:2px dotted var(--dots);margin:0 5px;transform:translateY(-4px);opacity:.9}
.price{color:var(--price)}
.desc{font-size:10px;font-style:italic;line-height:13.6px;padding-left:24px;padding-bottom:1px}
.photo{position:absolute;left:298px;top:552px;width:297px;height:296px;background:radial-gradient(ellipse at 45% 40%,#5a3524 0%,#3a2216 45%,#1e140f 80%),#2a1a12}
.pack{position:absolute;font-size:10px;font-style:italic;line-height:13.6px}
.pack h4{font-weight:400;font-style:normal;font-size:12.5px;color:var(--green);line-height:17px;margin-top:2px}
.pack p{padding-left:24px}
.pack .fine{font-size:6.5px;line-height:9px}
.ring-small{position:absolute;left:770px;top:132px}
.pack-price{position:absolute;left:770px;top:132px;width:92px;height:92px;display:flex;align-items:center;justify-content:center;font-family:"Great Vibes",cursive;font-size:38px;color:#fff}
.ring-big{position:absolute;left:596px;top:560px}
.delivery{position:absolute;left:612px;top:644px;font-family:"Great Vibes",cursive;color:#fff}
.delivery .big{font-size:52px;line-height:60px}
.delivery .small{font-size:36px;line-height:40px;margin-left:82px}
.note{position:absolute;left:605px;top:810px;font-size:9.5px;font-style:italic;line-height:14px}
.note span{display:block;padding-left:14px}
.brand{position:absolute;left:893px;top:230px;width:307px;display:flex;align-items:center;justify-content:center;gap:10px}
.brand-dot{width:18px;height:18px;border-radius:50%;background:var(--ring)}
.brand-name{font-weight:600;font-size:25px;line-height:32px;color:var(--green);white-space:nowrap}
.contact{position:absolute;left:893px;top:470px;width:307px;text-align:center}
.contact h2{font-family:"Oswald",sans-serif;font-weight:400;font-size:25px;letter-spacing:.5px;margin-top:8px}
.contact .tag{font-family:"Great Vibes",cursive;font-size:22px;line-height:25px;margin-top:12px}
.details{position:absolute;left:962px;top:614px;list-style:none;color:var(--green);font-size:16px;line-height:22.4px}
.details li{display:flex;gap:12px;margin-bottom:14px}
.details svg{flex:none;width:12px;height:12px;margin-top:5px}
</style>
</head>
<body>
<div class="flyer">

  <section class="section" style="left:0;top:0;width:297px;height:254px">
    <div class="bar">Ribs &amp; Wings</div>
    <div class="list" style="top:48px">
      <div class="row solo">Pork Ribs<span class="leader"></span><span class="price">$17.00</span></div>
      <div class="row solo">Beef Ribs<span class="leader"></span><span class="price">$15.00</span></div>
      <div class="row solo">Buffalo Wings<small>(6 Pcs)</small><span class="leader"></span><span class="price">$8.00</span></div>
      <div class="row solo">BBQ Wings<small>(6 Pcs)</small><span class="leader"></span><span class="price">$8.00</span></div>
      <div class="row solo">Honey Soy wings<small>(6 Pcs)</small><span class="leader"></span><span class="price">$8.00</span></div>
      <div class="row">Fried Wings<small>(6 Pcs)</small><span class="leader"></span><span class="price">$8.00</span></div>
      <p class="desc">with Tomato Sauce</p>
      <div class="row">Chicken Lollipop<small>(5 Pcs)</small><span class="leader"></span><span class="price">$8.00</span></div>
      <p class="desc">with Lemon Wedges</p>
    </div>
  </section>

  <section class="section" style="left:298px;top:0;width:297px;height:254px">
    <div class="bar">Drinks</div>
    <div class="list" style="top:48px">
      <div class="row">Can<span class="leader"></span><span class="price">$2.95</span></div>
      <p class="desc" style="padding-bottom:4px">Kola, Diet Kola, Kola Zero, Fizzo, Limo</p>
      <div class="row">1.25 lit<span class="leader"></span><span class="price">$4.95</span></div>
      <p class="desc" style="padding-bottom:4px">Kola, Diet Kola, Kola Zero, Fizzo, Limo</p>
      <div class="row solo">Leafton Ice Tea<span class="leader"></span><span class="price">$3.95</span></div>
      <div class="row solo">Orange Juice<span class="leader"></span><span class="price">$4.50</span></div>
      <div class="row solo">Ginger Beer<span class="leader"></span><span class="price">$3.95</span></div>
      <div class="row solo">Mount Fenwick Water<span class="leader"></span><span class="price">$2.50</span></div>
      <div class="row">Marrow Energy Drink (375 ml)<span class="leader"></span><span class="price">$3.95</span></div>
    </div>
  </section>

  <section class="section" style="left:596px;top:0;width:296px;height:254px">
    <div class="bar">Dinner Pack</div>
    <div class="pack" style="left:11px;top:46px">
      <h4>Pizza Pack</h4>
      <p>Cheesy Garlic Bread</p>
      <p>Any Large Pizza</p>
      <p class="fine">(Excl Premium range)</p>
      <p>Any Dessert or 1.25 lit</p>
      <h4>Pasta Pack</h4>
      <p>Curly Fries</p>
      <p>Any Pasta</p>
      <p>Any Dessert or 1.25 lit</p>
      <h4>Parmi Pack</h4>
      <p>Chips</p>
      <p>Any Parmigiana</p>
      <p>Any Dessert or 1.25 lit</p>
    </div>
    <div class="pack" style="left:160px;top:46px">
      <h4>Ribs &amp; Wings Pack</h4>
      <p>Chips</p>
      <p>Any Wings</p>
      <p>Ribs (Pork or Beef)</p>
    </div>
  </section>
  <svg class="ring-small" width="92" height="92" viewBox="0 0 92 92" aria-hidden="true">
    <circle cx="46" cy="46" r="41" fill="none" stroke="var(--ring)" stroke-width="6"/>
  </svg>
  <div class="pack-price">$25</div>

  <section class="section" style="left:0;top:256px;width:297px;height:314px">
    <div class="bar">The AB</div>
    <div class="list" style="top:46px">
      <div class="row">AB Chicken<span class="leader"></span><span class="price">$13.95</span></div>
      <p class="desc">Marinated Chicken,Cheese on Top of Fries<br>Drizzled with Ranch, BBQ &amp; Garlic Sauce</p>
      <div class="row">AB Meat L<span class="leader"></span><span class="price">$13.95</span></div>
      <p class="desc">Cheese, Pulled Beef, Bacon, Ham on Top<br>of Fries, Drizzled with Ranch, BBQ &amp;<br>Garlic Sauce</p>
      <div class="row">AB Combin<span class="leader"></span><span class="price">$13.95</span></div>
      <p class="desc">Cheese, Chicken, Pulled Beef, Ham on<br>Top of Fries, Drizzled with Ranch, BBQ<br>&amp; Garlic Sauce</p>
      <div class="row">AB Veg<span class="leader"></span><span class="price">$13.95</span></div>
      <p class="desc">Cheese, Tomato, Capsicum, Mushroom,<br>crumbed Fetta, Pineappleon Top of Fries,<br>Drizzled with Ranch, Tomato &amp; Garlic Sauce</p>
      <div class="row">AB Double<span class="leader"></span><span class="price">$11.95</span></div>
      <p class="desc">Double Cheese on Top of Fries, Drizzled<br>with Ranch, Tomato &amp; Garlic Sauce</p>
    </div>
  </section>

  <section class="section" style="left:298px;top:256px;width:297px;height:296px">
    <div class="bar">Dessert</div>
    <div class="list" style="top:46px">
      <div class="row solo">Chocolate Sundae<span class="leader"></span><span class="price">$4.95</span></div>
      <div class="row">Nocella Calzone<span class="leader"></span><span class="price">$6.00</span></div>
      <p class="desc">Calzone filled with Nocella &amp; topped<br>with Icing Sugar</p>
      <div class="row">Berry Zone<span class="leader"></span><span class="price">$9.00</span></div>
      <p class="desc">Nocella Calzone filled with Mixed Berry<br>&amp; topped with Icing Sugar</p>
      <div class="row">White Valcone<span class="leader"></span><span class="price">$9.00</span></div>
      <p class="desc">Calzone filled with White Chocolate &amp;<br>topped with Icing Sugar</p>
      <div class="row">Orbo Calzone<span class="leader"></span><span class="price">$9.00</span></div>
      <p class="desc">Calzone rolled with Orbo, filled with<br>White Chocolate &amp; topped with Icing Sugar</p>
      <div class="row">Tropical Calzone<span class="leader"></span><span class="price">$9.00</span></div>
      <p class="desc">Nocella Calzone filled with Mango<br>and Pineapple &amp; topped with Icing Sugar</p>
    </div>
  </section>
  <div class="photo" role="img" aria-label="Close-up photo of chocolate ice cream drizzled with chocolate sauce"></div>

  <section class="section" style="left:596px;top:256px;width:296px;height:592px">
    <div class="bar">Deals</div>
    <div class="list" style="top:50px">
      <div class="row">Party Deal<span class="leader"></span><span class="price">$54.95</span></div>
      <p class="desc">3 Large Pizza or Pasta<br>2 Garlic Bread<br>1.25 lit Drink</p>
      <div class="row">Family Deal<span class="leader"></span><span class="price">$39.95</span></div>
      <p class="desc">2 Large Pizza or Pasta<br>2 Garlic Bread<br>1.25 lit Drink</p>
      <div class="row">Couple Deal<span class="leader"></span><span class="price">$24.95</span></div>
      <p class="desc">1 Family Pizza<br>1 Garlic Bread<br>1.25 lit Drink</p>
      <div class="row">Single Deal<span class="leader"></span><span class="price">$19.95</span></div>
      <p class="desc">1 Large Pizza or Pasta<br>1 Garlic Bread<br>1 can drink</p>
      <div class="row">Small Deal<span class="leader"></span><span class="price">$14.95</span></div>
      <p class="desc">1 Small Pizza<br>1 Garlic Bread<br>1 can drink</p>
    </div>
  </section>
  <svg class="ring-big" width="296" height="288" viewBox="0 0 296 288" aria-hidden="true">
    <circle cx="196" cy="140" r="118" fill="none" stroke="var(--ring)" stroke-width="10"/>
  </svg>
  <div class="delivery">
    <div class="big">Free Delivery</div>
    <div class="small">$40 and over</div>
  </div>
  <p class="note">**(Large Pizza Excludes Premium &amp; Seafood range<span>One Offer per order )</span></p>

  <section class="section" style="left:0;top:572px;width:297px;height:276px">
    <div class="bar">Salad</div>
    <div class="list" style="top:46px">
      <div class="row">Garden Salad<span class="leader"></span><span class="price">$6.00</span></div>
      <p class="desc">Mixed Leaves, Tomato, Cucumber, Olives,<br>Onion, Cucumber, Pineapple &amp; Italian<br>dressing</p>
      <div class="row">Greek Salad<span class="leader"></span><span class="price">$6.00</span></div>
      <p class="desc">Mixed Leaves, Tomato, Cucumber, Olives,<br>Onion, Fetta &amp; Dressed with Lemon Juice,<br>Olive Oil, White wine vinegar</p>
      <div class="row">Coleslaw<span class="leader"></span><span class="price">$6.00</span></div>
      <p class="desc">Red Cabbages, Green Cabbage, Carrot,<br>Onion mixed with Mayonnaise and<br>Lemon</p>
      <div class="row">Chicken Ceaser Salad<span class="leader"></span><span class="price">$9.00</span></div>
      <p class="desc">Mixed Leaves, Chicken, Crispy Bacon,<br>Croutons, Parmesan Cheese &amp; Ceaser Dressing</p>
    </div>
  </section>

  <div class="brand">
    <span class="brand-dot"></span>
    <span class="brand-name">Brelvo Pizza &amp; Pasta</span>
  </div>

  <div class="contact">
    <h2>CONTACT US</h2>
    <p class="tag">We would love to hear it<br>from you</p>
  </div>

  <ul class="details">
    <li><svg viewBox="0 0 12 12" aria-hidden="true"><path d="M2.5 1 L4.5 1 L5.2 3.5 L4 4.5 Q5 7 7.5 8 L8.5 6.8 L11 7.5 L11 9.5 Q10 11 8.5 11 Q2 9.5 1 3.5 Q1 2 2.5 1Z" fill="var(--green)"/></svg>07 3048 2719</li>
    <li><svg viewBox="0 0 12 12" aria-hidden="true"><path d="M6 0.5 A4 4 0 0 1 10 4.5 C10 7 6 11.5 6 11.5 C6 11.5 2 7 2 4.5 A4 4 0 0 1 6 0.5Z" fill="var(--green)"/><circle cx="6" cy="4.5" r="1.6" fill="var(--bg)"/></svg><span>Brelvo Pizza &amp; Pasta<br>112 Harlow Park Rd<br>Wendmere</span></li>
    <li><svg viewBox="0 0 12 12" aria-hidden="true"><g fill="none" stroke="var(--green)" stroke-width="1"><circle cx="6" cy="6" r="5"/><ellipse cx="6" cy="6" rx="2.2" ry="5"/><path d="M1 6 H11 M2 3.3 H10 M2 8.7 H10"/></g></svg>www.brelvo.com.au</li>
  </ul>

</div>
</body>
</html>
```